Poster - Series of Poster Designs

We have a number of motivational quotes related to weight loss and fitness which need putting into a series of posters.
The designs need to:
- Reflect the current brand (see www.bluefernhaven.com.au)
- Be designed with scalability in mind to fit to A1, A3, A4, and A5. All portrait layout.
- Incorporate our logo
- Any images need to relfect the diversity of our clients ranging from 70kgs up to 200kgs.
- We have a stock of photos which can be used, or you can source your own (subject to budget approval)
Total of 26 posters in total, but all on the same design series (so effectively 1 design, with 26 applications).
The series of quotes are attached. An example quote would be:
-
"The difference between your body this week and next week is what you do for the next seven days to achieve your goals"
-
Our clients are a range of ages (20 - 60) and split male/female so colours should be neutral and reflect our orange/green branding. A modern feel but not super modern.
Output needs to be A3 ready to print with all source files included so that we can amend in the future.
There may be ongoing work for the right designer.

```html
<!DOCTYPE html>
<html lang="en">
<head>
<meta charset="utf-8">
<title>Bluefern Haven – What You Do</title>
<link rel="stylesheet" href="https://fonts.googleapis.com/css2?family=Montserrat:wght@700;800;900&display=swap">
<style>
  :root {
    --ink: #000000;
    --paper: #ffffff;
    --accent-red: #e3231f;
    --photo-light: #d4d4d4;
    --photo-mid: #8a8a8a;
    --photo-dark: #2e2e2e;
  }
  * { margin: 0; padding: 0; box-sizing: border-box; }
  html, body {
    width: 848px;
    height: 1200px;
    overflow: hidden;
    background: var(--ink);
  }
  .poster {
    position: relative;
    width: 848px;
    height: 1200px;
    background: var(--ink);
    font-family: "Montserrat", Arial, sans-serif;
    color: var(--paper);
    overflow: hidden;
  }
  .brand {
    position: absolute;
    top: 38px;
    left: 0;
    width: 100%;
    text-align: center;
  }
  .brand-name {
    font-weight: 800;
    font-size: 36px;
    letter-spacing: 0.5px;
    color: var(--paper);
    line-height: 1;
  }
  .photo {
    position: absolute;
    top: 262px;
    left: 0;
    width: 100%;
    height: 500px;
    background:
      radial-gradient(ellipse 55% 35% at 62% 22%, var(--photo-light) 0%, rgba(190,190,190,0.7) 45%, rgba(0,0,0,0) 85%),
      linear-gradient(to bottom, var(--ink) 0%, var(--photo-mid) 14%, var(--photo-dark) 45%, #111111 75%, var(--ink) 100%);
  }
  .quote-lead {
    position: absolute;
    top: 166px;
    left: 0;
    width: 100%;
    text-align: center;
    font-weight: 700;
    font-size: 34px;
    line-height: 44px;
    letter-spacing: 0.2px;
  }
  .quote-punch {
    position: absolute;
    top: 742px;
    left: 0;
    width: 100%;
    text-align: center;
    font-weight: 900;
    font-size: 166px;
    line-height: 146px;
    letter-spacing: -2px;
    text-transform: uppercase;
  }
  .quote-punch .line { display: block; }
  .quote-punch .emphasis { color: var(--accent-red); }
</style>
</head>
<body>
  <main class="poster">
    <header class="brand">
      <span class="brand-name">BLUEFERN HAVEN</span>
    </header>

    <div class="photo" role="img" aria-label="Black and white photo of a man and a woman training with boxing gloves and focus pads in a gym"></div>

    <p class="quote-lead">the difference between who you are and<br>what you want to be is</p>

    <h1 class="quote-punch">
      <span class="line">What</span>
      <span class="line">You</span>
      <span class="line emphasis">Do</span>
    </h1>
  </main>
</body>
</html>
```